Meridale Eating needs Stationary and a business card

We would like to use our current logo. The text can be moved around as needed. The stationary needs to be a 'first page' where the logo is more prominent to be impressive on higher quality paper and a second page where the logo is more subtle where there will be much more information on the page. There are 2 clinic locations which will need include name, address, phone number, fax number, web address. The business card should be single sided and contain this information also.
The design must be contemporary and sophisticated as this is a science based diet run out of a medical clinic.

Target Market(s)

People wanting to lose weight, athletes looking to optimise performance, people with arthritis or fighting cancer

Industry/Entity Type

Business

Contact Information for Business Card

must use the logo. I have attached an example card with the practice details on it. there must be space for the doctors name. Also the website www.meridaleeating.example.au

Requirements
Must have
• the logo, the business adresses and phone numbers, the website, the doctors name and qualifications
Nice to have
• some creativity
Should not have
• Do not simply reproduce the existing card please

```html
<!DOCTYPE html>
<html lang="en">
<head>
<meta charset="utf-8">
<title>Meridale Eating – Stationery</title>
<link rel="stylesheet" href="https://fonts.googleapis.com/css2?family=Open+Sans:wght@400;600&family=Saira+Condensed:wght@400;500&display=swap">
<style>
:root{
  --bg:#e6e7ea;
  --paper:#ffffff;
  --ink:#4a4d52;
  --navy:#1e4f86;
  --blue:#2f8fd6;
  --sky:#47b6ea;
  --mist:#e3f0fa;
  --faint:#d5dde6;
}
*{box-sizing:border-box;margin:0;padding:0}
html,body{width:1200px;height:1200px;overflow:hidden;background:var(--bg)}
body{position:relative;font-family:"Open Sans",sans-serif;color:var(--ink)}
.sheet{position:absolute;top:36px;width:540px;height:764px;background:var(--paper);overflow:hidden;box-shadow:0 4px 14px rgba(0,0,0,.18)}
.sheet--follow{left:40px}
.sheet--first{left:620px}
.brand{display:flex;align-items:center;gap:8px;font-weight:600;color:var(--navy)}
.brand__dot{width:34px;height:34px;border-radius:50%;background:var(--sky);flex:none}
.sheet--first .brand{position:absolute;left:44px;top:44px;font-size:19px}
.sheet--first .brand__dot{width:52px;height:52px}
.pattern{position:absolute;left:0;right:0;bottom:0;height:62%;background:linear-gradient(to bottom,rgba(227,240,250,0),var(--mist) 55%,#d4e8f7)}
.recipient{position:absolute;left:70px;top:150px;font-size:8.5px;line-height:1.5}
.letter{position:absolute;left:70px;top:215px;width:410px;font-size:8px;line-height:1.55}
.letter p{margin-bottom:10px}
.sheet-contacts{position:absolute;right:34px;bottom:30px;font-family:"Saira Condensed",sans-serif;font-size:12px;line-height:1.35;color:#2b2e33}
.sheet-contacts .loc{color:var(--blue);font-weight:500}
.sheet-contacts .svc{color:var(--blue)}
.vertical-name{position:absolute;left:8px;bottom:20px;transform-origin:left bottom;transform:rotate(-90deg) translate(0,100%);font-size:78px;font-weight:600;letter-spacing:2px;color:var(--faint);white-space:nowrap;line-height:1}
.rule{position:absolute;left:110px;top:70px;width:2px;height:640px;background:#cfe6f6}
.sheet--follow .letter{left:130px;top:90px;width:360px}
.card{position:absolute;left:320px;top:840px;width:560px;height:320px;background:linear-gradient(100deg,#fff 40%,#e6f2fb);overflow:hidden;box-shadow:0 4px 14px rgba(0,0,0,.2)}
.card .brand{position:absolute;left:30px;top:34px;flex-direction:column;align-items:flex-start;font-size:12px;gap:6px}
.card .brand__dot{width:60px;height:60px}
.card__wave{position:absolute;right:0;top:0;width:150px;height:320px}
.card__person{position:absolute;left:160px;top:48px}
.card__name{font-size:26px;color:var(--navy);font-weight:400}
.card__quals{font-family:"Saira Condensed",sans-serif;font-size:10px;color:#333;margin-top:2px}
.card__role{font-family:"Saira Condensed",sans-serif;font-size:13px;color:#333}
.card__contacts{position:absolute;left:30px;top:165px;font-family:"Saira Condensed",sans-serif;font-size:12px;line-height:1.3;color:#2b2e33}
.card__contacts .loc{color:var(--blue);font-weight:500;font-size:13px;margin-top:8px}
.card__contacts .svc{color:var(--blue)}
</style>
</head>
<body>

<section class="sheet sheet--follow">
  <div class="vertical-name">MERIDALE EATING</div>
  <div class="rule"></div>
  <div class="letter">
    <p>Contrary to popular belief, Lorem Ipsum is not simply random text. It has roots in a piece of classical Latin literature from 45 BC, making it over 2000 years old. Harold Wenvick, a Latin professor at Ashbury College in Ohio, looked up one of the more obscure Latin words, consectetur, from a Lorem Ipsum passage, and going through the cites of the word in classical literature, discovered the undoubtable source. Lorem Ipsum comes from sections 1.10.32 and 1.10.33 of "de Finibus Bonorum et Malorum" (The Extremes of Good and Evil) by Lucan Ostrel, written in 45 BC. This book is a treatise on the theory of ethics, very popular during the Renaissance. The first line of Lorem Ipsum comes from a line in section 1.10.32.</p>
    <p>The standard chunk of Lorem Ipsum used since the 1500s is reproduced below for those interested. Sections 1.10.32 and 1.10.33 are also reproduced in their exact original form.</p>
    <p>Contrary to popular belief, Lorem Ipsum is not simply random text. It has roots in a piece of classical Latin literature from 45 BC, making it over 2000 years old. Harold Wenvick, a Latin professor at Ashbury College in Ohio, looked up one of the more obscure Latin words, consectetur, from a Lorem Ipsum passage, and going through the cites of the word in classical literature, discovered the undoubtable source. Lorem Ipsum comes from sections 1.10.32 and 1.10.33 (The Extremes of Good and Evil), very popular during the Renaissance, from a line in section 1.10.32.</p>
    <p>Contrary to popular belief, Lorem Ipsum is not simply random text. It has roots in a piece of classical Latin literature from 45 BC, making it over 2000 years old. Harold Wenvick looked up one of the more obscure Latin words, consectetur, from a Lorem Ipsum passage, and discovered the undoubtable source. Lorem Ipsum comes from sections 1.10.32 and 1.10.33 (The Extremes of Good and Evil), very popular during the Renaissance, from a line in section 1.10.32.</p>
    <p>The standard chunk of Lorem Ipsum used since the 1500s is reproduced below. Sections 1.10.32 and 1.10.33 are also reproduced in their exact original form.</p>
  </div>
</section>

<section class="sheet sheet--first">
  <div class="pattern" role="img" aria-label="Soft blue repeating figure-in-circle background pattern"></div>
  <div class="brand"><span class="brand__dot"></span>Meridale Eating</div>
  <div class="recipient">There are many<br>variations of passages<br>of Lorem Ipsum available</div>
  <div class="letter">
    <p>Dear Sir,</p>
    <p style="margin-top:22px">Contrary to popular belief, Lorem Ipsum is not simply random text. It has roots in a piece of classical Latin literature from 45 BC, making it over 2000 years old. Harold Wenvick, a Latin professor at Ashbury College in Ohio, looked up one of the more obscure Latin words, consectetur, from a Lorem Ipsum passage, and going through the cites of the word in classical literature, discovered the undoubtable source. Lorem Ipsum comes from sections 1.10.32 and 1.10.33 of "de Finibus Bonorum et Malorum" (The Extremes of Good and Evil) by Lucan Ostrel, written in 45 BC. This book is a treatise on the theory of ethics, very popular during the Renaissance. The first line of Lorem Ipsum, "Lorem ipsum dolor sit amet..", comes from a line in section 1.10.32.</p>
    <p>The standard chunk of Lorem Ipsum used since the 1500s is reproduced below for those interested. Sections 1.10.32 and 1.10.33 from "de Finibus Bonorum et Malorum" are also reproduced in their exact original form, accompanied by English versions.</p>
    <p>Contrary to popular belief, Lorem Ipsum is not simply random text. It has roots in a piece of classical Latin literature from 45 BC, making it over 2000 years old. Harold Wenvick, a Latin professor at Ashbury College in Ohio, looked up one of the more obscure Latin words, consectetur, from a Lorem Ipsum passage, and going through the cites of the word in classical literature, discovered the undoubtable source. Lorem Ipsum comes from sections 1.10.32 and 1.10.33 of "de Finibus Bonorum et Malorum" (The Extremes of Good and Evil) by Lucan Ostrel, written in 45 BC, very popular during the Renaissance. The first line of Lorem Ipsum comes from a line in section 1.10.32.</p>
    <p style="margin-top:18px">Regards,</p>
  </div>
  <div class="sheet-contacts">
    <div class="loc">Westmere</div>
    <div>12-14 Harbour Lane, Westmere NSW 2199</div>
    <div><span class="svc">T.</span> 02 5550 1420 | <span class="svc">Shoulder &amp; Elbow</span> www.varnellortho.example.au</div>
    <div class="loc">Northgate</div>
    <div>88 Kellam Street, Northgate NSW 2068</div>
    <div><span class="svc">T.</span> 02 5550 3812 | <span class="svc">Knee Surgery</span> www.kneeclinic.example.au</div>
  </div>
</section>

<section class="card">
  <svg class="card__wave" viewBox="0 0 150 320" role="img" aria-label="Blue curved band with repeating figure-in-circle pattern">
    <defs>
      <linearGradient id="waveFill" x1="0" y1="0" x2="1" y2="1">
        <stop offset="0" stop-color="#5cc3f0"/>
        <stop offset="1" stop-color="#2a9ae0"/>
      </linearGradient>
    </defs>
    <path d="M150 0 H40 C40 60 30 110 70 170 C110 230 95 280 120 320 H150 Z" fill="url(#waveFill)"/>
    <path d="M40 0 C40 60 30 110 70 170 C110 230 95 280 120 320" fill="none" stroke="#1e78c4" stroke-width="3"/>
  </svg>
  <div class="brand"><span class="brand__dot"></span>Meridale Eating</div>
  <div class="card__person">
    <div class="card__name">Dr Elias Varnell</div>
    <div class="card__quals">MBBS (NSW) MBiomedE FRACS (Ortho) FAOrthA</div>
    <div class="card__role">Orthopaedic Surgeon</div>
  </div>
  <div class="card__contacts">
    <div class="loc">Westmere</div>
    <div>12-14 Harbour Lane, Westmere NSW 2199</div>
    <div>T. 02 5550 1420 | <span class="svc">Shoulder &amp; Elbow</span> www.varnellortho.example.au</div>
    <div class="loc">Northgate</div>
    <div>88 Kellam Street, Northgate NSW 2068</div>
    <div>T. 02 5550 3812 | <span class="svc">Knee Surgery</span> www.kneeclinic.example.au</div>
  </div>
</section>

</body>
</html>
```